ORVA CRM website - sleek, sophisticated, uplifting

ORVA Center for Regenerative Medicine is a cutting-edge medical clinic aimed at providing treatment for various chronic conditions and help people stave off the declines usually associated with aging. We utilize the latest technology in regenerative medicine to help people with autoimmune conditions, musculoskeletal problems and chronic pain, neurodegenerative conditions, male enhancement, facial rejuvenation and hair restoration, etc. We provide personalized medicine, through highly compassionate and competent doctors and staff.

please look at my current website which is not focused on regenerative medicine, but some contents can stay, as far as the philosophy of the treatment: www.plmwellnessgroup.example. But the reason I am changing the name of the clinic is because the focus of the medical practice is shifted entirely to "regenerative medicine" - using the body's own healing mechanism such as stem cells and growth factors...

Please DO NOT recycle old graphics and pictures. I want this site to be brand new, fresh and original.

Would like the website to be more sophisticated and nicer-looking than this website: www.vantrelo.example

Target Market(s)

People who care a great deal about their health (above age 35), wants to prevent declines in their looks and health as they are getting older. Generally high income sector of the society that can afford self-pay (no insurance accepted) expensive stem cell treatment ranging from $4000 to $20,000.

Industry/Entity Type

Healthcare

Coding

Coded - Design and coding required

Number of Pages Required

5+ page

Font styles to use
Sans Serif
Other font styles liked:
• Al Bayan, Avenir, Didot, Open Sans or Tsukushi A Round Gothic for central text, but may use Chalkboard for titles, or others as seen fit

Colors

Designer to choose colors to be used in the design.

Requirements
Must have
• Ultra modern look, very clean & sleek images and layout, portraying a sense of sophistication and confidence. Works beautifully well with existing logo. Give a sense that the clinic employs cutting-edge science, and provide highly competent & compassionate services.
• More sophisticated and nicer-looking than this website: www.vantrelo.example
Nice to have
• many pages and links to science articles
Should not have
• fonts too playful or hard to read.

```html
<!DOCTYPE html>
<html lang="en">
<head>
<meta charset="utf-8">
<title>ORVA Center for Regenerative Medicine</title>
<link href="https://fonts.googleapis.com/css2?family=Montserrat:wght@600;700;800&family=Open+Sans:wght@400;600;700&display=swap" rel="stylesheet">
<style>
:root{
  --yellow:#f6cf10;
  --gold:#c99a2f;
  --dark:#2d2d2d;
  --ink:#111;
  --white:#fff;
  --muted:#d6d6d6;
  --red:#d33;
}
*{box-sizing:border-box;margin:0;padding:0}
html,body{width:1200px;height:3448px;overflow:hidden}
body{position:relative;font-family:"Open Sans",Arial,sans-serif;color:var(--white);background:var(--dark)}
.abs{position:absolute}
.heading{font-family:"Montserrat",Arial,sans-serif;font-weight:700;text-transform:uppercase}
.btn{position:absolute;background:var(--yellow);color:var(--ink);font-family:"Montserrat",Arial,sans-serif;font-weight:700;font-size:14px;text-transform:uppercase;display:flex;align-items:center;justify-content:center;border-radius:3px}
.rule{position:absolute;left:530px;width:140px;height:3px;background:var(--white)}
.section-title{position:absolute;left:0;width:1200px;text-align:center;font-size:33px;color:var(--white)}

/* header */
.topbar{position:absolute;left:0;top:0;width:1200px;height:92px;background:linear-gradient(90deg,#b88a25,var(--gold) 50%,#b88a25);z-index:3}
.nav{position:absolute;top:36px;display:flex;gap:26px;font-size:14px;font-weight:700;text-transform:uppercase}
.nav-left{left:99px}
.nav-right{left:754px}
.brand{position:absolute;left:474px;top:-40px;width:252px;height:252px;border-radius:50%;background:var(--white);z-index:4;display:flex;align-items:flex-end;justify-content:center;padding-bottom:56px}
.brand-name{font-family:"Montserrat",Arial,sans-serif;font-weight:700;font-size:52px;color:var(--ink);letter-spacing:2px}

/* hero */
.hero{position:absolute;left:0;top:0;width:1200px;height:650px}
.hero-eyebrow{left:99px;top:232px;font-family:"Montserrat",Arial,sans-serif;font-weight:700;font-size:24px}
.hero-title{left:99px;top:276px;font-size:64px;line-height:68px;font-weight:800}
.dots{left:101px;top:526px;display:flex;gap:6px}
.dots span{width:13px;height:13px;border-radius:50%;background:var(--white)}
.dots span:first-child{background:var(--yellow)}

/* split sections */
.split{position:absolute;left:0;width:1200px;background:linear-gradient(90deg,var(--yellow) 50%,var(--gold) 50%)}
.badge{position:absolute;left:563px;width:74px;height:74px;border-radius:50%;background:var(--white)}

.welcome-photo{left:99px;top:890px;width:434px;height:294px;border-radius:22px;border:5px solid #c9a51a;background:linear-gradient(135deg,#d9d9d9,#9a9a9a)}
.welcome-lead{left:621px;top:892px;width:480px;font-size:15px;font-weight:700;line-height:24px}
.welcome-body{left:621px;top:962px;width:480px;font-size:12.5px;line-height:22px;text-align:justify}

/* services */
.service{position:absolute}
.service h3{font-family:"Montserrat",Arial,sans-serif;font-weight:700;font-size:18.5px;text-transform:uppercase;white-space:nowrap;margin-bottom:10px}
.service p{font-size:13px;line-height:22px;color:var(--muted)}
.service.left{text-align:right}
.icon{position:absolute;width:42px;height:42px;border:3px solid var(--white);border-radius:50%}

/* video */
.video{left:200px;top:2154px;width:800px;height:352px;border-radius:22px;border:5px solid #c9a51a;overflow:hidden;background:linear-gradient(135deg,#5a2e1c,#3a1f16 50%,#6b4a32)}
.play{left:567px;top:2278px;width:68px;height:50px;border-radius:12px;background:var(--red)}
.caption{left:205px;top:2449px;width:790px;height:52px;background:rgba(255,255,255,.92);color:var(--ink);font-size:24px;display:flex;align-items:center;padding-left:200px}

/* contact */
.contact{position:absolute;left:0;top:2620px;width:1200px;height:830px;background:radial-gradient(ellipse at 30% 40%,#3b4148,#1f2327 70%)}
.field{position:absolute;background:var(--white);border-radius:3px;color:var(--ink);font-size:12px;font-weight:600;padding:14px 14px}
.info{position:absolute;top:3141px;display:flex;align-items:center;gap:16px;font-size:15px}
.info i{width:46px;height:46px;border-radius:50%;background:var(--yellow);display:flex;align-items:center;justify-content:center}
.footer-nav{position:absolute;left:0;top:3254px;width:1200px;display:flex;justify-content:center;gap:26px;font-size:14px;font-weight:700;text-transform:uppercase}
.copyright{position:absolute;left:0;top:3398px;width:1200px;text-align:center;color:var(--ink);font-size:14px;font-weight:600}
</style>
</head>
<body>

<!-- Hero -->
<section class="hero">
  <svg class="abs" width="1200" height="650" style="left:0;top:0">
    <defs>
      <linearGradient id="heroTone" x1="0" y1="0" x2="1" y2="0">
        <stop offset="0" stop-color="#0c0c0c"/>
        <stop offset=".55" stop-color="#1d1d1d"/>
        <stop offset="1" stop-color="#6a5a56"/>
      </linearGradient>
    </defs>
    <polygon points="0,0 1200,0 1200,602 600,660 0,602" fill="url(#heroTone)" role="img" aria-label="Photo of a man's bare back with a highlighted sore shoulder"/>
  </svg>
  <p class="abs hero-eyebrow">Center For Regenerative Medicine</p>
  <h1 class="abs heading hero-title">Multi Faceted<br>Health</h1>
  <a class="btn" style="left:99px;top:437px;width:133px;height:55px">Read More</a>
  <div class="abs dots"><span></span><span></span><span></span><span></span><span></span></div>
</section>

<header class="topbar">
  <nav class="nav nav-left"><span>Home</span><span>Services</span><span>The Science</span><span>AXM</span><span>Blog</span></nav>
  <nav class="nav nav-right"><span>Professional-Grade Supplements</span><span style="margin-left:28px">Contact</span></nav>
</header>
<div class="brand"><span class="brand-name">ORVA</span></div>

<!-- Welcome -->
<section class="split" style="top:602px;height:720px;z-index:-1"></section>
<svg class="abs" width="1200" height="80" style="left:0;top:598px"><polygon points="0,4 600,62 1200,4 1200,0 0,0" fill="#1a1a1a"/></svg>
<div class="badge" style="top:648px"></div>
<h2 class="heading section-title" style="top:752px">Welcome to ORVA</h2>
<div class="rule" style="top:816px"></div>
<div class="abs welcome-photo" role="img" aria-label="Portrait of a smiling doctor in a white coat with a stethoscope"></div>
<p class="abs welcome-lead">Our health is multi-faceted, and our vibrancy is built on our biological, psychological and spiritual wellbeing.</p>
<p class="abs welcome-body">We provide a new kind of healthcare that represents the future: we foster health in a holistic, preventative, and science-driven manner. We utilize the most up-to-date scientific data, treat each person as a unique individual, with unique micronutrient requirements, genetic codes, gut flora compositions, history of toxic exposures, and hormone variations.</p>
<a class="btn" style="left:621px;top:1120px;width:133px;height:53px">Read More</a>

<!-- Services -->
<svg class="abs" width="1200" height="680" style="left:0;top:1250px">
  <polygon points="0,72 600,0 1200,72 1200,620 600,660 0,620" fill="var(--dark)"/>
  <circle cx="600" cy="440" r="120" fill="var(--yellow)"/>
  <path d="M600,320 A120,120 0 0 1 600,560 Z" fill="var(--gold)"/>
  <g stroke="#fff" stroke-width="2" fill="#fff">
    <line x1="478" y1="257" x2="582" y2="257"/><polygon points="474,257 484,252 484,262"/><polygon points="586,257 576,252 576,262"/>
    <line x1="618" y1="257" x2="723" y2="257"/><polygon points="614,257 624,252 624,262"/><polygon points="727,257 717,252 717,262"/>
    <line x1="436" y1="392" x2="480" y2="392"/><polygon points="432,392 442,387 442,397"/>
    <line x1="720" y1="392" x2="762" y2="392"/><polygon points="766,392 756,387 756,397"/>
    <line x1="390" y1="502" x2="486" y2="502"/><polygon points="386,502 396,497 396,507"/>
    <line x1="714" y1="502" x2="808" y2="502"/><polygon points="812,502 802,497 802,507"/>
  </g>
</svg>
<h2 class="heading section-title" style="top:1340px">Our Services</h2>
<div class="rule" style="top:1403px"></div>

<div class="service left" style="left:94px;top:1494px;width:320px"><h3>Hair Restoration</h3><p>Progresses of leaps and bounds have been made in science that can help us dissect.</p></div>
<div class="icon" style="left:428px;top:1486px" role="img" aria-label="Hair icon"></div>
<div class="service left" style="left:93px;top:1614px;width:270px"><h3>Facial Rejuvenation</h3><p>Progresses of leaps and bounds have been made in science.</p></div>
<div class="icon" style="left:384px;top:1621px" role="img" aria-label="Face icon"></div>
<div class="service left" style="left:92px;top:1724px;width:230px"><h3>Male Enhancement</h3><p>Progresses of leaps and bounds have been made in science.</p></div>
<div class="icon" style="left:340px;top:1731px" role="img" aria-label="Beard icon"></div>

<div class="service" style="left:791px;top:1494px;width:320px"><h3>Musculoskeletal Problems</h3><p>Progresses of leaps and bounds have been made in science that can help us dissect.</p></div>
<div class="icon" style="left:731px;top:1486px" role="img" aria-label="Joint icon"></div>
<div class="service" style="left:835px;top:1614px;width:270px"><h3>Neuro Degeneration</h3><p>Progresses of leaps and bounds have been made in science.</p></div>
<div class="icon" style="left:770px;top:1621px" role="img" aria-label="Neuron icon"></div>
<div class="service" style="left:876px;top:1724px;width:230px"><h3>Chronic Pain</h3><p>Progresses of leaps and bounds have been made in science.</p></div>
<div class="icon" style="left:816px;top:1731px" role="img" aria-label="Body pain icon"></div>

<!-- Video -->
<section class="split" style="top:1870px;height:780px;z-index:-1"></section>
<div class="badge" style="top:1913px"></div>
<h2 class="heading section-title" style="top:2030px">Our Video</h2>
<div class="rule" style="top:2094px"></div>
<div class="abs video" role="img" aria-label="Video thumbnail of a speaker in front of bookshelves"></div>
<div class="abs play"><svg width="68" height="50"><polygon points="27,15 27,35 45,25" fill="#fff"/></svg></div>
<div class="abs caption">Dr. Martin Hale, <em style="font-size:18px;margin-left:8px">Chairman/Founder - AXM</em></div>

<!-- Contact -->
<section class="contact" role="img" aria-label="Soft dark background of blurred cells"></section>
<svg class="abs" width="1200" height="90" style="left:0;top:2616px"><polygon points="0,0 1200,0 1200,28 600,84 0,28" fill="var(--gold)"/><polygon points="0,0 600,0 600,84 0,28" fill="var(--yellow)"/></svg>
<h2 class="heading section-title" style="top:2672px">Contact Us</h2>
<div class="rule" style="top:2740px"></div>
<p class="abs" style="left:0;top:2770px;width:1200px;text-align:center;font-size:15px;font-weight:600">Have a question? Fill out the form below and I will get back to you</p>
<div class="field" style="left:99px;top:2830px;width:490px;height:49px">Name</div>
<div class="field" style="left:612px;top:2830px;width:489px;height:49px">Email</div>
<div class="field" style="left:99px;top:2899px;width:1002px;height:99px">Message</div>
<a class="btn" style="left:531px;top:3019px;width:138px;height:48px">Send Now</a>

<div class="info" style="left:99px"><i><svg width="20" height="14"><rect x="1" y="1" width="18" height="12" fill="none" stroke="#fff" stroke-width="2"/><polyline points="1,1 10,8 19,1" fill="none" stroke="#fff" stroke-width="2"/></svg></i>info@orva.example</div>
<div class="info" style="left:368px"><i><svg width="14" height="20"><path d="M7 1a6 6 0 0 1 6 6c0 5-6 12-6 12S1 12 1 7a6 6 0 0 1 6-6z" fill="#fff"/><circle cx="7" cy="7" r="2.2" fill="var(--yellow)"/></svg></i>1420 Meridian Avenue Suite 300 Fairview CA 90210</div>
<div class="info" style="left:926px"><i><svg width="18" height="18"><path d="M4 1l4 4-2 3c1 2 3 4 5 5l3-2 4 4-3 3C8 17 1 10 1 4z" fill="#fff"/></svg></i>+1 555 014 2290</div>

<nav class="footer-nav"><span>Home</span><span>|</span><span>Company</span><span>|</span><span>Profile</span><span>|</span><span>Services</span><span>|</span><span>Longevity Medicine</span><span>|</span><span>Contact</span></nav>

<svg class="abs" width="1200" height="150" style="left:0;top:3298px"><polygon points="0,52 600,0 1200,52 1200,150 0,150" fill="var(--gold)"/><polygon points="0,52 600,0 600,150 0,150" fill="var(--yellow)"/></svg>
<p class="copyright">Copyrights @ 2018 ORVA. All Rights Reserved.</p>

</body>
</html>
```